Surgery Office Letterhead Design

I'm seeking new letterhead that will comprise all of our office locations and logo and other applicable information, per the following:

Office Locations:

Bluewater Institute for Oral & Facial Surgery at Cleburne
347 Amberly Lane
Cleburne, Texas 76058
Phone 817.392.4806
Fax 817.392.7734

Bluewater Institute for Oral & Facial Surgery at Stephenville
588 Quarry Hollow Parkway
Stephenville, Texas 76428
Phone 254.763.2248
Fax 254.763.2251

Bluewater Institute for Oral & Facial Surgery at Belton
715 West 9th Street
Belton, Texas 76537
Phone 254.481.6072
Fax 254.481.6079

Other Info to include:

www.bluewatermaxillo.example
hello@bluewatermaxillo.example

Industry/Entity Type

Medical

Font styles to use
Serif
Sans Serif

Requirements
Must have
• See Project Description

```html
<!DOCTYPE html>
<html lang="en">
<head>
<meta charset="utf-8">
<title>Bluewater Institute Letterhead</title>
<link href="https://fonts.googleapis.com/css2?family=Carlito:wght@400;700&family=Montserrat:wght@400;500;600&display=swap" rel="stylesheet">
<style>
  :root {
    --bg: #d3d3d3;
    --paper: #ffffff;
    --ink: #1a1a1a;
    --navy: #1f2d5c;
    --steel: #7388a8;
    --rule: #8fa3c2;
    --divider: #9aa3b5;
    --sig: #d9dce3;
  }
  * { margin: 0; padding: 0; box-sizing: border-box; }
  html, body { width: 1200px; height: 1200px; overflow: hidden; background: var(--bg); }
  .letterhead {
    position: absolute; left: 150px; top: 17px;
    width: 900px; height: 1166px;
    background: var(--paper);
    font-family: "Carlito", "Lato", sans-serif;
    color: var(--ink);
    overflow: hidden;
  }
  .brand {
    position: absolute; left: 92px; top: 82px;
    display: flex; align-items: center; gap: 12px;
  }
  .brand-dot { width: 14px; height: 14px; border-radius: 50%; background: var(--navy); }
  .brand-name {
    font-family: "Carlito", sans-serif; font-weight: 700; color: var(--navy);
    font-size: 30px; line-height: 1; letter-spacing: 0.3px;
  }
  .brand-name span { display: block; font-size: 15px; letter-spacing: 0.8px; margin-top: 3px; }
  .contact {
    position: absolute; left: 643px; top: 86px;
    font-family: "Montserrat", sans-serif; font-size: 12px; color: var(--ink);
  }
  .contact li { list-style: none; display: flex; align-items: center; gap: 6px; height: 21px; }
  .contact svg { width: 14px; height: 14px; }
  .header-rule { position: absolute; left: 382px; top: 134px; width: 448px; height: 1.5px; background: var(--rule); }
  .letter { position: absolute; left: 84px; top: 202px; width: 800px; font-size: 15.8px; line-height: 31px; white-space: nowrap; }
  .letter h1 { font-size: 16px; font-weight: 700; line-height: 31px; margin-bottom: 31px; }
  .letter p { margin-bottom: 31px; }
  .signature { display: block; width: 194px; height: 70px; background: var(--sig); border-radius: 4px; margin: 11px 0 11px 9px; }
  .offices {
    position: absolute; left: 0; top: 1003px; width: 900px; height: 90px;
    font-family: "Montserrat", sans-serif; font-size: 12px; color: var(--ink);
  }
  .office { position: absolute; top: 0; line-height: 15px; }
  .office h2 { font-size: 14px; font-weight: 600; color: var(--navy); margin-bottom: 6px; }
  .office .lines { margin-bottom: 8px; }
  .office .tel { display: flex; align-items: center; gap: 7px; line-height: 16px; }
  .office svg { width: 13px; height: 11px; fill: var(--navy); }
  .office-marlow { left: 88px; }
  .office-cedarbrook { left: 374px; }
  .office-alderton { left: 697px; }
  .divider { position: absolute; top: 1005px; width: 1px; height: 85px; background: var(--divider); }
  .band { position: absolute; left: 0; bottom: 0; width: 900px; height: 42px; }
</style>
</head>
<body>
<main class="letterhead">
  <header>
    <div class="brand">
      <div class="brand-dot"></div>
      <div class="brand-name">Bluewater Institute<span>for Maxillofacial Care</span></div>
    </div>
    <ul class="contact">
      <li><svg viewBox="0 0 14 14"><rect x="1" y="3" width="12" height="9" fill="none" stroke="#1f2d5c" stroke-width="1.4"/><path d="M1 3l6 5 6-5" fill="none" stroke="#1f2d5c" stroke-width="1.4"/></svg>hello@bluewatermaxillo.example</li>
      <li><svg viewBox="0 0 14 14"><g fill="none" stroke="#1f2d5c" stroke-width="1.1"><circle cx="7" cy="7" r="6"/><ellipse cx="7" cy="7" rx="2.6" ry="6"/><path d="M1 7h12M2 4h10M2 10h10"/></g></svg>www.bluewatermaxillo.example</li>
    </ul>
    <div class="header-rule"></div>
  </header>

  <article class="letter">
    <h1>Lorem Ipsum is simply</h1>
    <p>&nbsp;dummy text of the printing and typesetting industry. Lorem Ipsum has been the industry's standard<br>dummy text ever since the 1500s, when an unknown printer took a galley of type and scrambled it to<br>make a type specimen book. It has survived not only five centuries, but also the leap into electronic<br>typesetting, remaining essentially unchanged. It was popularised in the 1960s with the release of Pressmark<br>sheets containing Lorem Ipsum passages, and more recently with desktop publishing software like Folio<br>Layout including versions of Lorem Ipsum.</p>
    <p>It is a long established fact that a reader will be distracted by the readable content of a page when look-<br>ing at its layout. The point of using Lorem Ipsum is that it has a more-or-less normal distribution of<br>letters, as opposed to using 'Content here, content here.</p>
    <p>&nbsp;Contrary to popular belief, Lorem Ipsum is not simply random text. It has roots in a piece of classical<br>Latin literature from 45 BC, making it over 2000 years old. Harold Wemberly, a Latin professor at Ash-<br>grove College in Virginia, looked up one of the more obscure Latin words, consectetur, from a<br>Lorem Ipsum passage,</p>
    <div class="closing">Lorem Ipsum</div>
    <span class="signature" role="img" aria-label="Handwritten signature"></span>
    <div class="signer">Lorem Ipsum is a dummy</div>
  </article>

  <section class="offices">
    <div class="office office-marlow">
      <h2>Marlow</h2>
      <div class="lines">347 Amberly Lane<br>Marlow, Texas 76058</div>
      <div class="tel"><svg viewBox="0 0 13 11"><path d="M1 4c0-2 3-3 5.5-3S12 2 12 4l-2.5 1L8.5 3.5h-4L3.5 5z"/><rect x="3" y="6" width="7" height="4" rx="1"/></svg>817.392.4806</div>
      <div class="tel"><svg viewBox="0 0 13 11"><rect x="3" y="0" width="7" height="4"/><rect x="1" y="4" width="11" height="7" rx="1"/></svg>817.392.7734</div>
    </div>
    <div class="office office-cedarbrook">
      <h2>Cedarbrook</h2>
      <div class="lines">588 Quarry Hollow Parkway<br>Cedarbrook, Texas 76428</div>
      <div class="tel"><svg viewBox="0 0 13 11"><path d="M1 4c0-2 3-3 5.5-3S12 2 12 4l-2.5 1L8.5 3.5h-4L3.5 5z"/><rect x="3" y="6" width="7" height="4" rx="1"/></svg>254.763.2248</div>
      <div class="tel"><svg viewBox="0 0 13 11"><rect x="3" y="0" width="7" height="4"/><rect x="1" y="4" width="11" height="7" rx="1"/></svg>254.763.2251</div>
    </div>
    <div class="office office-alderton">
      <h2>Alderton</h2>
      <div class="lines">715 West 9th Street<br>Alderton, Texas 76537</div>
      <div class="tel"><svg viewBox="0 0 13 11"><path d="M1 4c0-2 3-3 5.5-3S12 2 12 4l-2.5 1L8.5 3.5h-4L3.5 5z"/><rect x="3" y="6" width="7" height="4" rx="1"/></svg>254.481.6072</div>
      <div class="tel"><svg viewBox="0 0 13 11"><rect x="3" y="0" width="7" height="4"/><rect x="1" y="4" width="11" height="7" rx="1"/></svg>254.481.6079</div>
    </div>
  </section>
  <div class="divider" style="left:336px"></div>
  <div class="divider" style="left:654px"></div>

  <svg class="band" viewBox="0 0 900 42" preserveAspectRatio="none" aria-hidden="true">
    <path d="M565 0H900V42H632C612 22 592 8 565 0Z" fill="var(--steel)"/>
    <path d="M0 0H500C555 0 595 18 618 42H0Z" fill="var(--navy)"/>
  </svg>
</main>
</body>
</html>
```